WordPress Direct-Booking Website for Bend, Oregon Vacation Rental — $750 Budget
Project Overview

We are looking for a talented WordPress designer/developer to create a clean, professional and inviting direct-booking website for Cedar Lantern Retreat, an established short-term vacation rental in Bend, Oregon.

The property is currently successfully listed on Staynest and Lodgr. Our Staynest property has approximately a 4.98-star rating with more than 200 reviews, is an Staynest Guest Pick, and ranks among the Top 1% of eligible homes.

Project Budget: $750

We will select the designer based on the quality of the initial concept, understanding of the property, proposed booking solution and ability to deliver a completed and functioning WordPress website.

Existing Staynest Listing

Please use our current Staynest listing as the primary reference for photographs, property details, amenities and design inspiration:

https://www.staynest.example/rooms/48170356

Original high-resolution photographs and additional property information will be provided to the selected designer.

Design Direction

We want the website to feel:

Upscale but comfortable
Warm and welcoming
Clean and uncluttered
Pacific Northwest / Central Oregon
Professional rather than corporate
Highly visual with large property photographs
Easy to navigate
Excellent on phones, tablets and desktop computers

We welcome creativity and want designers to show us their vision for the property rather than simply copying our Staynest listing.

The website should immediately communicate that Cedar Lantern Retreat is a highly rated vacation rental in an excellent Bend location.

Key Property Features
3 bedrooms
2 bathrooms
Sleeps up to 6 guests
Pet friendly
Approximately a 5-minute walk to Bend's Tanager Quarter
Near restaurants, shopping and Brightwater Lawn Pavilion
Private fenced backyard
Covered outdoor area
Off-street driveway parking
Fireplace
Well-equipped kitchen
Staynest Premier Host
Staynest Guest Pick
Top 1% of eligible Staynest homes
Approximately 4.98 stars with 200+ guest reviews

Our location, guest reviews, cleanliness, comfort, backyard, pet-friendly accommodations and walkability should be major selling points throughout the website.

Website Structure

We anticipate approximately 6–7 pages:

Home

Large hero photograph with a strong opening message and prominent BOOK DIRECT and CHECK AVAILABILITY buttons.

The home page should quickly communicate:

CEDAR LANTERN RETREAT — BEND, OREGON

3 Bedrooms | 2 Baths | Sleeps 6 | Pet Friendly | Walk to Tanager

Our exceptional guest rating and Staynest history should also be prominently featured.

The House

Bedrooms, bathrooms, kitchen, living areas, backyard and major amenities.

Photo Gallery

Large, attractive and fast-loading photographs with an easy-to-use mobile gallery.

Location / Explore Bend

Tanager Quarter, Brightwater Lawn Pavilion, Kettleback River, restaurants, breweries, shopping, downtown Bend and nearby outdoor recreation.

Guest Reviews

Selected guest reviews and prominent presentation of our strong Staynest reputation.

Availability & Book Direct

A simple and professional direct-booking experience.

Contact / FAQ

Contact information plus common questions regarding pets, parking, check-in/check-out, cancellations and other policies.

IMPORTANT — Direct Booking & Credit Card Requirements

We want guests to be able to book directly through the website without having to contact us first.

The website should use a proven WordPress vacation-rental booking plugin or system rather than a custom-built reservation/payment system.

Guests should be able to:

Select arrival and departure dates
See available dates
Enter number of guests
See nightly charges
See cleaning fees
See applicable lodging taxes and other charges
See the complete reservation total before paying
Enter guest/contact information
Pay securely by credit or debit card
Receive an automatic reservation confirmation

Paywell is our preferred credit-card processor.

Credit-card information must be processed securely through Paywell or another established payment processor. Credit-card information should NOT be stored directly on our WordPress website.

Staynest & Lodgr Calendar Synchronization

This is very important.

The direct-booking calendar must synchronize with our existing Staynest and Lodgr calendars to reduce the possibility of double bookings.

For this single-property website, we prefer a simple solution using Staynest/Lodgr calendar or iCal synchronization rather than an expensive monthly channel-management service, if practical.

The designer should clearly identify the booking plugin/system they propose using.

IMPORTANT — Tell Us Your Proposed Booking Solution

As part of your submission, please tell us:

Which WordPress booking plugin/system you recommend.
Whether it synchronizes availability with Staynest and Lodgr.
Whether it integrates directly with Paywell.
The initial cost of the plugin/software.
Any annual or monthly fees.
Whether any additional paid software or services will be required.

We strongly prefer a solution with little or no ongoing monthly software expense.

We do not want to select a designer and later discover that the proposed booking system requires an expensive monthly subscription.

WordPress & Technical Requirements

The completed project should include:

Fully functioning WordPress website
Responsive desktop/tablet/mobile design
Fast-loading pages
Optimized photographs
SSL/HTTPS compatibility
Direct-booking functionality
Paywell payment integration
Staynest calendar synchronization
Lodgr calendar synchronization
Automatic booking confirmations
Cleaning fee and lodging-tax calculations
Contact form
Wayfind Maps/location integration
Basic spam/security protection
Wayfind Metrics capability
Basic SEO setup
Search-engine submission capability
Easy owner editing of text, rates and photographs
Search Engine Optimization

The website should be structured for Wayfind and other search engines.

Important search themes include:

Bend Oregon vacation rental
Bend Oregon vacation home
Tanager Quarter vacation rental
Vacation rental near Tanager Bend
Bend Oregon pet-friendly vacation rental
Bend vacation rental near Brightwater Lawn Pavilion
Bend Oregon direct booking vacation rental

We are not expecting an extensive ongoing SEO campaign for the $750 project. We do expect proper page titles, descriptions, headings, image optimization and a good technical foundation for future SEO.

Ownership

Upon completion and final payment:

We own the completed WordPress website.
We receive full WordPress administrator access.
We control the domain and hosting accounts.
We own all custom design files created for the project.
All necessary login credentials are provided to us.
The website can be moved to another WordPress hosting provider in the future.
There should be no proprietary dependency on the developer after completion.
What We Want From Contestants

Please review our Staynest listing before submitting your concept.

We are particularly interested in seeing an initial homepage concept showing how you would present:

Cedar Lantern Retreat
The Bend / Tanager location
Our photography
Our exceptional guest reviews and ratings
The Book Direct message
The availability/booking call-to-action

We will provide feedback on the concepts we like and work with the selected designer to refine and complete the website.

Our Goal

Our objective is straightforward:

Create a beautiful, trustworthy and easy-to-use website that encourages guests to book Cedar Lantern Retreat directly with us.

The website will complement—not replace—our existing Staynest and Lodgr listings.

We want repeat guests and new customers to have an easy way to find the property, check availability and book directly while receiving the same professional experience they expect from a major vacation-rental platform.

Target Market(s)

Consumers looking to to travel to Mexico for vacation. Family or couples

Industry/Entity Type

Short term vacation rental industry

Coding

Coded - Design and coding required

Number of Pages Required

5+ page

Requirements
Must have
• Capabilities to accept credit card payments and link to other rental property sites calendars such as LODGR and Staynets
Nice to have
• Option for best plugins for property rental

```html
<!DOCTYPE html>
<html lang="en">
<head>
<meta charset="utf-8">
<title>Cedar Lantern Retreat · Bend, Oregon</title>
<link href="https://fonts.googleapis.com/css2?family=Libre+Caslon+Text:wght@400&family=Montserrat:wght@400;500;600;700&display=swap" rel="stylesheet">
<style>
:root{
  --green:#3e4b36;
  --green-dark:#2f3a29;
  --cream:#f6f3ee;
  --cream-2:#efebe4;
  --ink:#2b2b28;
  --muted:#5c5a55;
  --line:#ddd7cd;
  --orange:#c4522a;
  --star:#e8891d;
  --white:#ffffff;
}
*{margin:0;padding:0;box-sizing:border-box}
html,body{width:800px;height:1200px;overflow:hidden;background:var(--cream)}
body{font-family:"Montserrat",sans-serif;color:var(--ink);position:relative}
.serif{font-family:"Libre Caslon Text",serif}
section,header,footer{position:absolute;left:0;width:800px}
.ph{position:absolute}

/* hero */
.hero{top:0;height:281px;overflow:hidden}
.hero .ph{inset:0;background:linear-gradient(90deg,#1d2019 0%,#2a2a26 30%,rgba(90,70,70,.6) 55%,#6b5a63 70%,#3f4148 100%),linear-gradient(180deg,#b66a6a 0%,#55505a 45%,#2b2d24 100%)}
.hero .shade{position:absolute;inset:0;background:linear-gradient(90deg,rgba(20,22,18,.85) 0%,rgba(20,22,18,.45) 40%,rgba(20,22,18,0) 65%)}
.brand{position:absolute;left:38px;top:18px;display:flex;align-items:center;gap:8px;color:var(--white)}
.brand .dot{width:14px;height:14px;border-radius:50%;background:var(--white)}
.brand .name{font-family:"Libre Caslon Text",serif;font-size:14px;letter-spacing:.3px;line-height:1}
.brand .place{font-size:6.5px;letter-spacing:2px;margin-top:4px;padding-left:30px}
.nav{position:absolute;left:283px;top:24px;display:flex;gap:16px;font-size:8.5px;font-weight:500;color:var(--white);letter-spacing:.3px}
.nav .on{border-bottom:1px solid var(--white);padding-bottom:4px}
.btn{display:inline-flex;align-items:center;justify-content:center;gap:6px;font-weight:600;letter-spacing:.5px;text-transform:uppercase}
.book-direct{position:absolute;left:697px;top:18px;width:81px;height:27px;background:var(--green);color:var(--white);font-size:8px}
.hero h1{position:absolute;left:38px;top:86px;font-family:"Libre Caslon Text",serif;font-weight:400;font-size:28px;line-height:32px;color:var(--white)}
.facts{position:absolute;left:38px;top:197px;font-size:10.5px;font-weight:500;color:var(--white);letter-spacing:.4px}
.hero .cta{position:absolute;top:226px;height:31px;font-size:9px}
.cta.primary{left:38px;width:142px;background:var(--green);color:var(--white)}
.cta.ghost{left:191px;width:140px;border:1px solid var(--white);color:var(--white)}

/* stats */
.stats{top:281px;height:102px;background:var(--cream);display:flex;padding:14px 20px 0}
.stat{flex:1;text-align:center;border-right:1px solid var(--line);height:76px}
.stat:last-child{border-right:0}
.stat svg{display:block;margin:0 auto 5px;height:22px}
.stat .big{font-size:14px;font-weight:600;letter-spacing:.5px;line-height:1.1}
.stat .big.num{font-size:15px}
.stat .sm{font-size:7px;line-height:1.8;color:var(--ink)}
.stat .stars{color:var(--star);font-size:9px;letter-spacing:1px}

/* welcome */
.welcome{top:383px;height:223px;background:var(--cream)}
.welcome .copy{position:absolute;left:37px;top:19px;width:195px}
.eyebrow{font-size:7px;font-weight:500;letter-spacing:.6px;text-transform:uppercase}
.welcome h2{font-family:"Libre Caslon Text",serif;font-weight:400;font-size:17px;line-height:20px;margin:10px 0 10px}
.welcome p{font-size:7px;line-height:12.8px;color:var(--ink)}
.small-btn{position:absolute;height:22px;background:var(--green);color:var(--white);font-size:6.5px;padding:0 9px}
.welcome .small-btn{left:37px;top:164px;width:133px}
.img-living{left:246px;top:1px;width:341px;height:222px;background:linear-gradient(135deg,#d9d4cc,#b7aa98 55%,#8f7f6a)}
.img-kitchen{left:591px;top:2px;width:195px;height:104px;background:linear-gradient(135deg,#e7e2d8,#b69a7a)}
.img-bed{left:591px;top:108px;width:195px;height:115px;background:linear-gradient(135deg,#dfdbd3,#c5bba9 60%,#5f8580)}

/* amenities */
.amenities{top:606px;height:63px;background:var(--cream);display:flex;padding:6px 20px 0}
.amen{flex:1;text-align:center;border-right:1px solid var(--line);height:52px;font-size:7px;font-weight:500;text-transform:uppercase;line-height:10px}
.amen:last-child{border-right:0}
.amen svg{display:block;margin:2px auto 6px;height:22px}

/* bend */
.bend{top:669px;height:177px;background:var(--cream)}
.img-bend{left:0;top:0;width:373px;height:177px;background:linear-gradient(180deg,#7a5a7a 0%,#d17a56 35%,#3a3a3c 65%,#1c1f22 100%)}
.bend .copy{position:absolute;left:401px;top:16px;width:380px}
.bend h2{font-family:"Libre Caslon Text",serif;font-weight:400;font-size:17px;margin-top:8px}
.near{display:flex;margin-top:16px}
.near div{width:91px;text-align:center;font-size:6px;line-height:10.5px;color:var(--muted)}
.near svg{display:block;margin:0 auto 6px;height:20px}
.near b{display:block;font-size:8px;color:var(--ink);font-weight:600;margin-bottom:2px}
.bend .small-btn{left:402px;top:149px;width:84px;height:20px}

/* pets */
.pets{top:846px;height:111px;background:var(--cream)}
.pets .badge{position:absolute;left:30px;top:23px;width:48px;height:48px;border-radius:50%;background:var(--cream-2);display:flex;align-items:center;justify-content:center}
.pets h2{position:absolute;left:105px;top:27px;font-family:"Libre Caslon Text",serif;font-weight:400;font-size:17px}
.pets .kick{position:absolute;left:105px;top:52px;font-size:7px;font-weight:500;letter-spacing:.3px}
.pets p{position:absolute;left:105px;top:76px;width:200px;font-size:7px;line-height:12.5px}
.img-yard{left:298px;top:1px;width:502px;height:110px;background:linear-gradient(90deg,#3b3e40 0%,#4a4a46 40%,#7a6a4a 70%,#3f4a2a 100%)}

/* reviews */
.reviews{top:957px;height:151px;background:var(--white)}
.reviews h2{position:absolute;top:4px;width:100%;text-align:center;font-family:"Libre Caslon Text",serif;font-weight:400;font-size:17px}
.reviews .score{position:absolute;top:26px;width:100%;text-align:center;font-size:9px}
.reviews .score span{color:var(--star);letter-spacing:1px;margin-right:5px}
.arrow{position:absolute;top:1025px;width:16px;height:16px;border-radius:50%;border:1px solid var(--line);background:var(--white)}
.card{position:absolute;top:38px;height:76px;background:var(--white);box-shadow:0 1px 4px rgba(0,0,0,.1);padding:8px 10px 0 30px;font-size:6.2px;line-height:9.8px}
.card .mk{position:absolute;left:10px;top:9px;width:11px;height:11px;border-radius:50%;border:1.3px solid var(--orange)}
.card .st{color:var(--star);font-size:8px;letter-spacing:1px;line-height:9px;margin-bottom:3px}
.card .who{margin-top:4px}
.proof{position:absolute;top:122px;display:flex;gap:10px;font-size:6.2px;line-height:9px}
.proof .sh{width:22px;height:22px;border-radius:50%;background:#d7c39a}
.proof b{font-size:7px;display:block}

/* booking */
.booking{top:1108px;height:56px;background:var(--green)}
.booking h2{position:absolute;left:26px;top:5px;font-family:"Libre Caslon Text",serif;font-weight:400;font-size:13px;color:var(--white)}
.booking p{position:absolute;left:26px;top:24px;font-size:7.5px;line-height:11px;color:var(--white);width:190px}
.form{position:absolute;left:229px;top:6px;width:526px;height:32px;background:var(--white);display:flex;align-items:center}
.field{position:relative;height:24px;padding:2px 0 0 19px;border-right:1px solid var(--line);font-size:5.5px;font-weight:600}
.field span{display:block;font-size:8px;font-weight:400;color:var(--muted);margin-top:3px}
.field svg{position:absolute;right:8px;top:7px}
.form .go{margin-left:auto;margin-right:8px;width:118px;height:22px;background:var(--orange);color:var(--white);font-size:7.5px}
.trust{position:absolute;top:44px;left:310px;display:flex;gap:40px;font-size:5.8px;color:var(--white);font-weight:500}
.trust i{display:inline-block;width:6px;height:6px;border-radius:50%;background:#d9a441;margin-right:5px;vertical-align:-1px}

/* footer */
.foot{top:1164px;height:36px;background:var(--green-dark);color:var(--white);font-size:5.5px;line-height:7.5px}
.foot .brand{top:8px;left:44px}
.foot .brand .name{font-size:11px}
.foot .brand .place{font-size:5px;padding-left:22px;margin-top:3px}
.foot .brand .dot{width:10px;height:10px}
.col{position:absolute;top:6px}
.col b{font-size:6px;font-weight:600;display:block;margin-bottom:1px}
</style>
</head>
<body>

<header class="hero">
  <div class="ph" role="img" aria-label="Dusk photograph of the grey craftsman house with flowering shrubs, stone steps and a detached two-car garage"></div>
  <div class="shade"></div>
  <div class="brand">
    <div class="dot"></div>
    <div><div class="name">CEDAR LANTERN RETREAT</div><div class="place">BEND, OREGON</div></div>
  </div>
  <nav class="nav"><span class="on">THE HOUSE</span><span>PHOTOS</span><span>LOCATION</span><span>REVIEWS</span><span>AVAILABILITY</span><span>FAQ</span><span>CONTACT</span></nav>
  <a class="btn book-direct">Book Direct</a>
  <h1>Your Bend getaway<br>just steps from<br>the Tanager.</h1>
  <div class="facts">3 BEDROOMS &nbsp;•&nbsp; 2 BATHS &nbsp;•&nbsp; SLEEPS 6 &nbsp;•&nbsp; PET FRIENDLY</div>
  <a class="btn cta primary"><svg width="10" height="10" viewBox="0 0 10 10" fill="none" stroke="#fff" stroke-width="1"><rect x="1" y="2" width="8" height="7"/><path d="M1 4h8M3 1v2M7 1v2"/></svg>Check Availability</a>
  <a class="btn cta ghost">Explore the House</a>
</header>

<section class="stats">
  <div class="stat">
    <svg viewBox="0 0 20 20" width="20"><path d="M10 1l2.6 6 6.4.5-4.9 4.2 1.5 6.3L10 14.6 4.4 18l1.5-6.3L1 7.5 7.4 7z" fill="var(--green)"/></svg>
    <div class="big num">4.98</div><div class="sm">205 GUEST REVIEWS</div><div class="stars">★★★★★</div>
  </div>
  <div class="stat">
    <svg viewBox="0 0 40 22" width="40"><circle cx="20" cy="11" r="8" fill="none" stroke="#8a7a55" stroke-width="1.5"/></svg>
    <div class="big">TOP 1%</div><div class="sm">OF STAYNEST HOMES<br>Top 1% of eligible homes</div>
  </div>
  <div class="stat">
    <svg viewBox="0 0 22 22" width="22"><circle cx="11" cy="11" r="8" fill="none" stroke="var(--orange)" stroke-width="1.5"/></svg>
    <div class="big">GUEST PICK</div><div class="sm">Highly rated stay<br>Staynest Guest Pick</div>
  </div>
  <div class="stat">
    <svg viewBox="0 0 22 22" width="22"><path d="M11 20s-6-6.5-6-11a6 6 0 0 1 12 0c0 4.5-6 11-6 11z" fill="none" stroke="var(--green)" stroke-width="1.6"/><circle cx="11" cy="9" r="2.2" fill="var(--green)"/></svg>
    <div class="big">5 MIN WALK</div><div class="sm">TO TANAGER QUARTER<br>Shops, dining &amp; river trails</div>
  </div>
  <div class="stat">
    <svg viewBox="0 0 22 22" width="22"><rect x="4" y="3" width="14" height="16" rx="2" fill="var(--green)"/></svg>
    <div class="big">PREMIER HOST</div><div class="sm">5.0 CLEANLINESS<br>5.0 LOCATION</div>
  </div>
</section>

<section class="welcome">
  <div class="copy">
    <div class="eyebrow">Welcome to Cedar Lantern Retreat</div>
    <h2>Stay close to everything.<br>Feel away from it all.</h2>
    <p>Cedar Lantern Retreat is a beautifully updated 3 bedroom, 2 bath home just a 5-minute walk to Bend's Tanager Quarter. Enjoy a fenced backyard, cozy fireplace, well-equipped kitchen and everything you need for an unforgettable Bend getaway.</p>
  </div>
  <a class="btn small-btn">Learn More About the House</a>
  <div class="ph img-living" role="img" aria-label="Living room with wood stove on a stone hearth, two cream sofas and a tufted leather ottoman"></div>
  <div class="ph img-kitchen" role="img" aria-label="Bright kitchen with stainless appliances and a set dining table"></div>
  <div class="ph img-bed" role="img" aria-label="Bedroom with a queen bed, chandelier and teal dresser"></div>
</section>

<section class="amenities">
  <div class="amen"><svg viewBox="0 0 24 24" width="24" fill="none" stroke="var(--green)" stroke-width="1.8"><rect x="3" y="3" width="18" height="18"/><path d="M7 21v-9h10v9M12 19c-2 0-2.5-2-1-4 .3 1 1 1.3 1.5.5.5 1.5 1 3.5-.5 3.5z"/></svg>Fireplace</div>
  <div class="amen"><svg viewBox="0 0 24 24" width="24" fill="none" stroke="var(--green)" stroke-width="2"><path d="M5 3v18M10 3v18M15 3v18M20 3v18M2 8h20M2 16h20"/></svg>Fenced Backyard</div>
  <div class="amen"><svg viewBox="0 0 24 24" width="24" fill="var(--green)"><ellipse cx="12" cy="16" rx="5" ry="4"/><circle cx="5" cy="10" r="2.2"/><circle cx="9.5" cy="6" r="2.2"/><circle cx="14.5" cy="6" r="2.2"/><circle cx="19" cy="10" r="2.2"/></svg>Pet Friendly</div>
  <div class="amen"><svg viewBox="0 0 24 24" width="24" fill="var(--green)"><rect x="4" y="9" width="16" height="10" rx="2"/><rect x="2" y="7" width="20" height="2"/><rect x="10" y="4" width="4" height="2"/></svg>Fully Equipped<br>Kitchen</div>
  <div class="amen"><svg viewBox="0 0 24 24" width="24" fill="none" stroke="var(--green)" stroke-width="2"><path d="M3 17v-5l2-5h14l2 5v5zM3 17v3M21 17v3M3 12h18"/><circle cx="7" cy="14.5" r="1" fill="var(--green)"/><circle cx="17" cy="14.5" r="1" fill="var(--green)"/></svg>Private Parking</div>
  <div class="amen"><svg viewBox="0 0 24 24" width="24"><path d="M12 22s-7-7.5-7-12.5a7 7 0 0 1 14 0C19 14.5 12 22 12 22z" fill="none" stroke="var(--green)" stroke-width="2"/><circle cx="12" cy="9.5" r="2.5" fill="var(--green)"/></svg>Walk to<br>Tanager</div>
</section>

<section class="bend">
  <div class="ph img-bend" role="img" aria-label="Riverside lodge at sunset with two smokestacks, pines and lights reflecting on the water"></div>
  <div class="copy">
    <div class="eyebrow">The best of Bend, right outside your door</div>
    <h2>Bend is right outside your door.</h2>
    <div class="near">
      <div><svg viewBox="0 0 20 20" width="20" fill="var(--green)"><rect x="3" y="7" width="14" height="12" rx="1"/><path d="M7 7V5a3 3 0 0 1 6 0v2" fill="none" stroke="var(--green)" stroke-width="1.6"/></svg><b>5 MIN</b>Tanager Quarter<br>Shops, dining<br>&amp; entertainment</div>
      <div><svg viewBox="0 0 20 20" width="20" fill="var(--green)"><path d="M7 3l10-2v12" fill="none" stroke="var(--green)" stroke-width="1.8"/><path d="M7 3v13" stroke="var(--green)" stroke-width="1.8"/><circle cx="5" cy="16" r="2.5"/><circle cx="15" cy="14" r="2.5"/></svg><b>5 MIN</b>Brightwater Lawn<br>Pavilion<br>Concerts &amp; events</div>
      <div><svg viewBox="0 0 22 20" width="22" fill="none" stroke="var(--green)" stroke-width="1.6"><path d="M2 5c3-2 6 2 9 0s6-2 9 0M2 10c3-2 6 2 9 0s6-2 9 0M2 15c3-2 6 2 9 0s6-2 9 0"/></svg><b>NEARBY</b>Kettleback River<br>Trails, parks &amp;<br>outdoor adventure</div>
      <div><svg viewBox="0 0 20 20" width="20" fill="var(--green)"><rect x="3" y="5" width="7" height="14"/><rect x="10" y="2" width="7" height="17"/></svg><b>MINUTES</b>Downtown Bend<br>Breweries, dining<br>&amp; local charm</div>
    </div>
  </div>
  <a class="btn small-btn">Explore Bend</a>
</section>

<section class="pets">
  <div class="badge"><svg viewBox="0 0 24 24" width="24" fill="none" stroke="var(--ink)" stroke-width="1.4"><ellipse cx="12" cy="16" rx="5" ry="4"/><circle cx="5" cy="10" r="2.2"/><circle cx="9.5" cy="6" r="2.2"/><circle cx="14.5" cy="6" r="2.2"/><circle cx="19" cy="10" r="2.2"/></svg></div>
  <h2>Bring your best friend.</h2>
  <div class="kick">CEDAR LANTERN RETREAT IS PET FRIENDLY.</div>
  <p>Our fully fenced backyard gives your pup room to play while you relax and enjoy Bend.</p>
  <div class="ph img-yard" role="img" aria-label="Evening backyard with lit fence, lawn, patio umbrella and string lights"></div>
</section>

<section class="reviews">
  <h2>Guests Love Cedar Lantern Retreat</h2>
  <div class="score"><span>★★★★★</span>4.98 from 205 reviews</div>
  <div class="card" style="left:109px;width:183px"><i class="mk"></i><div class="st">★★★★★</div>“Perfect location! We walked to the Tanager every day and loved having a quiet place to come back to. The backyard is amazing and our dog had the best time.”<div class="who">Tessa • Portland, OR • May 2024</div></div>
  <div class="card" style="left:302px;width:188px"><i class="mk"></i><div class="st">★★★★★</div>“Spotless, comfortable and so well stocked. Everything was just as described and communication was excellent.” We will definitely stay again!”<div class="who">Owen • Seattle, WA • April 2024</div></div>
  <div class="card" style="left:502px;width:184px"><i class="mk"></i><div class="st">★★★★★</div>“Beautiful home in an unbeatable location. The walk to the Tanager is so easy and the neighborhood is quiet and safe.” Highly recommend!”<div class="who">Maren • Boise, ID • March 2024</div></div>
  <div class="proof" style="left:139px"><i class="sh"></i><div><b>Guest Pick</b>One of the most loved<br>homes on Staynest</div></div>
  <div class="proof" style="left:333px"><i class="sh" style="border-radius:4px"></i><div><b>Top 1%</b>of eligible homes<br>on Staynest</div></div>
  <div class="proof" style="left:509px"><i class="sh" style="width:12px;border-radius:2px"></i><div><b>PREMIER HOST</b>Consistently rated 5 stars<br>by our guests</div></div>
</section>
<svg class="arrow" style="left:75px" viewBox="0 0 16 16"><path d="M9 5L6 8l3 3" fill="none" stroke="#333" stroke-width="1"/></svg>
<svg class="arrow" style="left:703px" viewBox="0 0 16 16"><path d="M7 5l3 3-3 3" fill="none" stroke="#333" stroke-width="1"/></svg>

<section class="booking">
  <h2>Ready for your Bend getaway?</h2>
  <p>Book direct and make Cedar Lantern Retreat your home base for exploring Bend.</p>
  <div class="form">
    <div class="field" style="width:130px">CHECK IN<span>Add dates</span><svg width="10" height="10" viewBox="0 0 10 10" fill="none" stroke="#555"><rect x="1" y="2" width="8" height="7"/><path d="M1 4h8"/></svg></div>
    <div class="field" style="width:132px">CHECK OUT<span>Add dates</span><svg width="10" height="10" viewBox="0 0 10 10" fill="none" stroke="#555"><rect x="1" y="2" width="8" height="7"/><path d="M1 4h8"/></svg></div>
    <div class="field" style="width:130px;border-right:0">GUESTS<span>1 guest</span><svg width="10" height="10" viewBox="0 0 10 10" fill="none" stroke="#555"><path d="M2 4l3 3 3-3"/></svg></div>
    <a class="btn go">Check Availability</a>
  </div>
  <div class="trust"><span><i></i>Best Price Guaranteed</span><span><i></i>No Service Fees</span><span><i></i>Secure Booking</span></div>
</section>

<footer class="foot">
  <div class="brand">
    <div class="dot"></div>
    <div><div class="name">CEDAR LANTERN RETREAT</div><div class="place">BEND, OREGON</div></div>
  </div>
  <div class="col" style="left:249px"><b>QUICK LINKS</b>The House<br>Photos<br>Location</div>
  <div class="col" style="left:343px;top:13px">Reviews<br>Availability<br>FAQ</div>
  <div class="col" style="left:458px"><b>CONTACT</b>(555) 014-2270<br>hello@cedarlanternretreat.example<br>Bend, Oregon</div>
  <div class="col" style="left:625px"><b>FOLLOW US</b>Snapline &nbsp; Circlebook</div>
</footer>

</body>
</html>
```